Solar Company Bussiness Card

I need a 2 sided business card and would like a .psd and any font files for each side of the card. I would like my logo used, it should be attached with the fonts. I'm not opposed to the font colors with the logo being changed.

On the sample design, I'd like the following:

Martin Halloway
President
Phone: 555-318-4907
www.brightvanepower.example

As I've recently opened in a 2nd market, I'm not sure about an address as I currently have 2 of them. I may actually get separate cards printed, one batch for each address, that's why I need the PSD file.
Updates

I'm very pleased with the response and designs I've received here for my business card. First and foremost, I'd like to thank everyone who took the time to submit a design. There truly are a lot of great designs in the bunch here and I'm having a little difficulty deciding. I will be reaching out to someone in the next day or two here to go to a final design. At this time, I'm not looking for any new concepts. If any of you do logos, I'm looking for a new logo for our sister entity, Halloway Partners, Inc. Thanks, Martin Halloway

Reason: I'm not looking for any new designs at this point, but extending this deadline in order to give people I've asked a chance to re-submit items.

Industry/Entity Type

Business

```html
<!DOCTYPE html>
<html lang="en">
<head>
<meta charset="utf-8">
<title>Brightvane Power – Business Card</title>
<link rel="stylesheet" href="https://fonts.googleapis.com/css2?family=Source+Sans+3:wght@400;600;700&display=swap">
<style>
  :root {
    --page-bg: #e9eaec;
    --card-dark: #0d0d0d;
    --glow-gold: #6a4c14;
    --gold: #d9a63a;
    --card-light: #ffffff;
    --brand-blue: #1762b3;
    --shadow: rgba(0, 0, 0, 0.28);
  }
  * { margin: 0; padding: 0; box-sizing: border-box; }
  html, body {
    width: 1003px;
    height: 1200px;
    overflow: hidden;
    background: var(--page-bg);
    font-family: "Source Sans 3", "Myriad Pro", sans-serif;
  }
  .canvas {
    position: relative;
    width: 1003px;
    height: 1200px;
  }
  .card {
    position: absolute;
    left: 49px;
    box-shadow: 0 6px 14px var(--shadow);
    overflow: hidden;
  }
  /* Front */
  .card-front {
    top: 51px;
    width: 908px;
    height: 533px;
    background: var(--card-dark);
  }
  .front-texture {
    position: absolute;
    inset: 0;
    background:
      radial-gradient(ellipse 42% 48% at 46% 52%, rgba(150, 108, 32, 0.75) 0%, rgba(90, 64, 18, 0.35) 45%, rgba(0, 0, 0, 0) 100%),
      linear-gradient(160deg, #1c1c1c 0%, #0a0a0a 55%, #151515 100%);
  }
  .front-brand {
    position: absolute;
    left: 0;
    right: 0;
    top: 222px;
    display: flex;
    align-items: center;
    justify-content: center;
    gap: 22px;
  }
  .front-brand .mark {
    width: 58px;
    height: 58px;
    background: var(--gold);
  }
  .front-brand .name {
    font-size: 78px;
    font-weight: 600;
    line-height: 1;
    color: var(--gold);
    letter-spacing: 0.5px;
  }
  /* Back */
  .card-back {
    top: 611px;
    width: 912px;
    height: 534px;
    background: var(--card-light);
  }
  .back-brand {
    position: absolute;
    right: 40px;
    top: 40px;
    display: flex;
    align-items: center;
    gap: 14px;
  }
  .back-brand .mark {
    width: 38px;
    height: 38px;
    background: var(--brand-blue);
  }
  .back-brand .name {
    font-size: 48px;
    font-weight: 600;
    line-height: 1;
    color: var(--brand-blue);
  }
  .band {
    position: absolute;
    left: 0;
    right: 0;
    background: var(--brand-blue);
  }
  .band-top { top: 133px; height: 20px; }
  .band-bottom { top: 494px; height: 40px; }
  .person-name {
    position: absolute;
    left: 50px;
    top: 262px;
    font-size: 60px;
    font-weight: 700;
    letter-spacing: 2.5px;
    color: var(--brand-blue);
    text-transform: uppercase;
    line-height: 1;
  }
  .contact {
    position: absolute;
    left: 57px;
    top: 370px;
    list-style: none;
    font-size: 21px;
    font-weight: 700;
    line-height: 29px;
    letter-spacing: 0.8px;
    color: var(--brand-blue);
    text-transform: uppercase;
  }
</style>
</head>
<body>
<main class="canvas">
  <section class="card card-front" aria-label="Card front">
    <div class="front-texture" role="img" aria-label="Dark diagonal stripe texture with a warm gold glow"></div>
    <div class="front-brand">
      <span class="mark"></span>
      <span class="name">Brightvane Power</span>
    </div>
  </section>

  <section class="card card-back" aria-label="Card back">
    <div class="back-brand">
      <span class="mark"></span>
      <span class="name">Brightvane Power</span>
    </div>
    <div class="band band-top"></div>
    <h1 class="person-name">Martin Halloway</h1>
    <ul class="contact">
      <li>President</li>
      <li>Phone: 555-318-4907</li>
      <li>www.brightvanepower.example</li>
    </ul>
    <div class="band band-bottom"></div>
  </section>
</main>
</body>
</html>
```